PEACFUL ACUPUNCTURE PRACTITIONER NEEDS A NEW COAT

I need a new design for an exiting website http://willowgateneedlework.com/ for a acupuncturist. This will be a minimalism design with lots and lots of white space. Home page and one interior page. Please keep the feeling of calm and peaceful serenity. For Color scheme: https://www.morningfernclinic.com/fertility. The bottom part of the home page with sections and links to the service pages: https://harborlotuswellness.com/. The client likes this the best: http://mfclinic.com/. I'm attaching the logo and content pages.

Target Market(s)

Women

Industry/Entity Type

Wellness, health, wellbeing, meditation

Number of Pages Required

2 page

Font styles to use
Sans Serif
Decorative

Colors

Designer to choose colors to be used in the design.

Requirements
Must have
Nice to have
• Follow new website drafts and links
Should not have
• Busy with bright colors. No poping

```html
<!DOCTYPE html>
<html lang="en">
<head>
<meta charset="utf-8">
<title>About — Willowgate Acupuncture</title>
<link href="https://fonts.googleapis.com/css2?family=Gelasio:ital,wght@0,400;0,700;1,700&family=Montserrat:wght@400;500&family=Pinyon+Script&display=swap" rel="stylesheet">
<style>
:root{
  --backdrop:#e0dccb;
  --page:#ffffff;
  --ink:#4a4a48;
  --muted:#b4af97;
  --muted-sans:#b8b4a3;
  --blush:#f3e3e6;
  --rose:#c99aa3;
  --tile:#f2f0ec;
  --band:#f8f7f4;
  --footer:#f2f1ec;
  --rule:#d9d6cc;
  --button:#b9b49d;
}
*{margin:0;padding:0;box-sizing:border-box}
html,body{width:806px;height:1200px;overflow:hidden}
body{background:var(--backdrop);position:relative;font-family:"Gelasio",Georgia,serif;color:var(--muted)}
.page{position:absolute;left:110px;top:0;width:586px;height:1200px;background:var(--page)}
.abs{position:absolute}
/* header */
.brand{left:133px;top:13px;display:flex;align-items:center;gap:5px}
.brand-dot{width:18px;height:18px;border-radius:50%;background:var(--rose);opacity:.75}
.brand-name{font-family:"Gelasio",serif;font-size:11px;color:var(--ink);font-weight:400}
.nav{top:16px;left:513px;display:flex;gap:14px;font-size:8px;color:var(--ink)}
.nav a{color:inherit;text-decoration:none}
.nav .current{text-decoration:underline;text-underline-offset:3px;text-decoration-color:var(--muted)}
.nav svg{vertical-align:middle;margin-left:3px}
.menu{left:657px;top:16px;width:16px}
.menu span{display:block;height:1px;background:var(--ink);margin-bottom:4px}
/* sections */
.initial{font-family:"Pinyon Script",cursive;color:var(--blush);font-size:52px;line-height:1}
.heading{font-family:"Gelasio",serif;font-style:italic;font-weight:700;color:var(--ink);font-size:9.5px}
.copy{font-size:6.7px;line-height:10px;color:var(--muted)}
.portrait{left:137px;top:234px;width:201px;height:164px;border-radius:5px;
  background:linear-gradient(135deg,#f3d89a 0%,#e9c27a 40%,#f6e3b6 70%,#f0d8a0 100%)}
.tile{background:var(--tile);border-radius:3px}
.clinic-mark{left:139px;top:700px;width:164px;display:flex;flex-direction:column;align-items:center;gap:6px}
.clinic-mark .brand-dot{width:30px;height:30px}
.clinic-mark .brand-name{font-size:14px;text-align:center}
/* consult band */
.consult{left:110px;top:823px;width:586px;height:82px;background:var(--band)}
.consult h2{position:absolute;top:18px;width:100%;text-align:center;font-style:italic;font-weight:700;font-size:10.5px;color:var(--muted);letter-spacing:.2px}
.consult p{position:absolute;left:66px;top:36px;width:450px;font-family:"Montserrat",sans-serif;font-size:9.2px;line-height:12.5px;color:var(--muted-sans)}
.consult strong{font-weight:500;color:var(--muted)}
/* footer */
.footer{left:110px;top:1012px;width:586px;height:188px;background:var(--footer)}
.f-head{font-weight:700;font-size:8px;color:var(--ink);letter-spacing:.2px}
.hours{left:131px;top:1052px;width:144px;font-family:"Montserrat",sans-serif;font-size:6px;color:var(--muted-sans)}
.hours li{list-style:none;display:flex;justify-content:space-between;height:18.5px;padding-top:6px;border-bottom:1px solid var(--rule)}
.feed{left:330px;top:1055px;width:147px;display:grid;grid-template-columns:repeat(3,47.5px);grid-auto-rows:40px;gap:1.5px}
.feed div{border-radius:1px}
.socials-label{left:330px;top:1150px;width:147px;text-align:center;font-family:"Montserrat",sans-serif;font-size:7px;color:var(--muted-sans)}
.socials{left:364px;top:1164px;display:flex;gap:13px}
.socials span{width:8px;height:8px;border-radius:50%;border:1px solid #8f8c82}
.news-text{left:528px;top:1053px;width:110px;font-family:"Montserrat",sans-serif;font-size:5.8px;line-height:10px;color:var(--muted-sans)}
.subscribe{left:528px;top:1080px;display:flex}
.subscribe .field{width:108px;height:17px;background:#fff;font-family:"Montserrat",sans-serif;font-size:5px;color:#b8b6ae;padding:6px 7px}
.subscribe .btn{width:38px;height:17px;background:var(--button);color:#fff;font-family:"Montserrat",sans-serif;font-size:5.5px;font-weight:500;text-align:center;line-height:17px}
.contacts{left:528px;top:1146px;font-family:"Montserrat",sans-serif;font-size:6px;line-height:11.3px;color:var(--ink)}
.contacts a{color:var(--muted-sans)}
</style>
</head>
<body>
<div class="page"></div>

<header>
  <div class="abs brand"><span class="brand-dot"></span><span class="brand-name">Willowgate Acupuncture</span></div>
  <nav class="abs nav">
    <a href="#">Home</a>
    <a href="#" class="current">About</a>
    <a href="#">Treatments<svg width="6" height="4" viewBox="0 0 6 4"><path d="M.5.5 3 3 5.5.5" fill="none" stroke="#4a4a48" stroke-width=".8"/></svg></a>
  </nav>
  <div class="abs menu"><span></span><span></span><span></span></div>
</header>

<section class="practitioner">
  <div class="abs initial" style="left:121px;top:124px">M</div>
  <h2 class="abs heading" style="left:139px;top:148px">Mara</h2>
  <div class="abs copy" style="left:139px;top:161px;width:506px">
    <p>Marian Ellery is a Massachusetts and California Licensed Acupuncturist and Herbalist as well as Nationally Certified in both Acupuncture and Herbal Medicine. She obtained her Masters Degree from Seven Rivers University in Santa Cruz CA and has studied at the integrated hospital in Hang Zhou China.</p>
    <p>She has also done extensive study in Chi Nei Tsang in both the USA and Thailand.</p>
    <p>She worked for Linden Herb Company a leader of high quality, lab tested Chinese patented herbal formulas as a consultant to both Acupuncturists and Western MD's.</p>
    <p>Every year Mara commits to attending in person and virtual educational events in order to grow as a practitioner and human being.</p>
  </div>

  <div class="abs portrait" role="img" aria-label="Portrait photo of the practitioner in front of a warm striped curtain"></div>

  <div class="abs initial" style="left:357px;top:217px">A</div>
  <h2 class="abs heading" style="left:375px;top:241px">Area of Focus</h2>
  <div class="abs copy" style="left:375px;top:254px;width:136px">
    <p>“I have focused on hormonal health and fertility through bodywork, acupuncture and herbal medicine for decades.</p>
    <p>A fascination with how the hormonal feedback loops of our bodies can be accessed through the patterns of Acupuncture led me towards an obsession with fertility and conception.</p>
    <p>I began my training with Dr. Helen Zhao in San Francisco in 1998. After completing my Masters Degree at SRU and then further study in China, I returned to CA to work with the team at Cradle Acupuncture and Coastal Reproductive Partners. In</p>
  </div>
  <div class="abs copy" style="left:527px;top:254px;width:138px">
    <p>&nbsp;2011 I returned to the East Coast to be closer to my family and began my private practice.</p>
    <p>Every year I commit to continue my learning through both online classes and conferences.</p>
    <p>I love my work so you will often find me in the office! But I can also be found hiking, camping, reading, eating vegetables, sitting quietly, feeding the birds while avoiding bears, traveling, laughing at good jokes and enjoying time with my animal, human and extended friend family.</p>
  </div>
</section>

<section class="office-dog">
  <div class="abs initial" style="left:121px;top:436px">J</div>
  <h2 class="abs heading" style="left:139px;top:459px">Dr. Juniper Day</h2>
  <div class="abs copy" style="left:139px;top:472px;width:510px">
    <p>Juniper came up from Florida in July of 2020. After some (alot) training she began practicing and is currently in charge of operations (not really.) She prefers chin scratches to head scratches and has never met a treat she didn't like. She never enters treatment rooms and air filters are constantly on to combat dander. If you would prefer not to meet Juniper just call ahead and she can retire to her dog office (locked kennel.)</p>
  </div>
</section>

<section class="clinic">
  <div class="abs initial" style="left:121px;top:572px">A</div>
  <h2 class="abs heading" style="left:139px;top:595px">About the Clinic</h2>
  <div class="abs copy" style="left:139px;top:608px;width:166px">
    <p>Willowgate Acupuncture is a small clinic off the beaten path in downtown Easthaven, MA. Treatments take place in a private, relaxed and quiet setting. Private, non metered parking is available right outside the door.</p>
  </div>
  <div class="abs clinic-mark"><span class="brand-dot"></span><span class="brand-name">Willowgate Acupuncture</span></div>
  <div class="abs tile" style="left:314px;top:604px;width:177px;height:178px"></div>
  <div class="abs tile" style="left:497px;top:604px;width:85px;height:86px"></div>
  <div class="abs tile" style="left:589px;top:604px;width:85px;height:86px"></div>
  <div class="abs tile" style="left:497px;top:697px;width:85px;height:85px"></div>
  <div class="abs tile" style="left:589px;top:697px;width:85px;height:85px"></div>
</section>

<section class="abs consult">
  <h2>SCHEDULE A FREE 30 MINUTE CONSULTATION</h2>
  <p>Consultations are always available to help answer any questions you may have about acupuncture or herbal medicine in a relaxed environment. <strong>555-014-3827</strong></p>
</section>

<footer>
  <div class="abs footer"></div>
  <h3 class="abs f-head" style="left:131px;top:1034px">HOUR</h3>
  <ul class="abs hours">
    <li><span>Monday</span><span>Closed</span></li>
    <li><span>Tuesday</span><span>10 am - 6.30 pm</span></li>
    <li><span>Wednesday</span><span>10 am - 6.30 pm</span></li>
    <li><span>Thursday</span><span>10 am - 6.30 pm</span></li>
    <li><span>Friday</span><span>1 pm - 6.30 pm</span></li>
    <li><span>Saturday</span><span>10 am - 3 pm</span></li>
    <li><span>Sunday</span><span>Closed</span></li>
  </ul>

  <h3 class="abs f-head" style="left:330px;top:1034px">INSTAGRAM FEED</h3>
  <div class="abs feed">
    <div role="img" aria-label="Photo of a pregnant woman holding her belly" style="background:linear-gradient(135deg,#efe9e4,#d8c9bd)"></div>
    <div role="img" aria-label="Photo of an acupuncture treatment on a back" style="background:linear-gradient(135deg,#e6ddd2,#cdbfae)"></div>
    <div role="img" aria-label="Photo of a woman relaxing during a facial treatment" style="background:linear-gradient(135deg,#cfd3c4,#d9b8a4)"></div>
    <div role="img" aria-label="Photo of hands giving a massage" style="background:linear-gradient(135deg,#c9a98a,#e0c8b0)"></div>
    <div role="img" aria-label="Photo of a smiling woman in a white robe" style="background:linear-gradient(135deg,#e8ddd3,#d6bfae)"></div>
    <div role="img" aria-label="Photo of a woman holding white flowers" style="background:linear-gradient(135deg,#eeeae2,#c9c2b1)"></div>
  </div>
  <div class="abs socials-label">Our Socials</div>
  <div class="abs socials"><span></span><span></span><span></span><span></span></div>

  <h3 class="abs f-head" style="left:528px;top:1034px">NEWSLETTER</h3>
  <p class="abs news-text">To find out what's new and our new treatments in preview.</p>
  <div class="abs subscribe"><div class="field">Email Address</div><div class="btn">Subscribe</div></div>

  <h3 class="abs f-head" style="left:528px;top:1130px">CONTACTS</h3>
  <div class="abs contacts">
    <div>Email: <a href="#">mara@willowgateneedlework.com</a></div>
    <div>Address: <a href="#">48 Alder Row Easthaven, MA 01099</a></div>
    <div>Phone: <a href="#">555-014-3827</a></div>
  </div>
</footer>
</body>
</html>
```